Checkout sign

Wall sign for clinic checkout.
“The Good Lord does ALL the healing..
But we DO collect the co-pay”

Add Celtic cross at top and our logo on bottom

```html
<!DOCTYPE html>
<html lang="en">
<head>
<meta charset="utf-8">
<title>Checkout Sign – Dunleavy Orthopedic Clinic</title>
<link rel="preconnect" href="https://fonts.googleapis.com">
<link href="https://fonts.googleapis.com/css2?family=Cinzel:wght@400;600&display=swap" rel="stylesheet">
<style>
  :root {
    --page-bg: #e4e4e4;
    --sign-blue: #1c008c;
    --sign-white: #ffffff;
    --ornament-tone: #8f80c6;
  }
  html, body {
    margin: 0;
    padding: 0;
    width: 1200px;
    height: 1200px;
    overflow: hidden;
    background: var(--page-bg);
  }
  .canvas {
    position: relative;
    width: 1200px;
    height: 1200px;
    font-family: "Cinzel", "Trajan Pro", serif;
    color: var(--sign-white);
  }
  .sign-disc {
    position: absolute;
    inset: 0;
  }
  .cross-ornament {
    position: absolute;
    left: 479px;
    top: 183px;
    width: 242px;
    height: 242px;
    border-radius: 50%;
    background: radial-gradient(circle, var(--sign-white) 0%, var(--ornament-tone) 100%);
  }
  .slogan {
    position: absolute;
    left: 0;
    top: 462px;
    width: 1200px;
    margin: 0;
    text-align: center;
    font-weight: 400;
    font-size: 50px;
    line-height: 64px;
    letter-spacing: 1px;
  }
  .slogan .strong {
    font-weight: 600;
  }
  .slogan span {
    display: block;
  }
  .clinic-mark {
    position: absolute;
    left: 507px;
    top: 755px;
    width: 186px;
    height: 186px;
    border-radius: 50%;
    border: 5px solid var(--sign-white);
    box-sizing: border-box;
  }
  .clinic-name {
    position: absolute;
    left: 0;
    top: 932px;
    width: 1200px;
    text-align: center;
    font-weight: 400;
    font-size: 60px;
    line-height: 60px;
    letter-spacing: 1px;
  }
  .clinic-type {
    position: absolute;
    left: 0;
    top: 990px;
    width: 1200px;
    text-align: center;
    font-weight: 400;
    font-size: 26px;
    line-height: 30px;
    letter-spacing: 2px;
  }
</style>
</head>
<body>
  <main class="canvas">
    <svg class="sign-disc" width="1200" height="1200" viewBox="0 0 1200 1200" aria-hidden="true">
      <circle cx="600" cy="602" r="503" fill="var(--sign-blue)"/>
      <circle cx="600" cy="602" r="480" fill="none" stroke="var(--sign-white)" stroke-width="4"/>
      <circle cx="600" cy="602" r="468" fill="none" stroke="var(--sign-white)" stroke-width="2"/>
    </svg>

    <div class="cross-ornament" role="img" aria-label="Celtic knotwork cross inside a ring"></div>

    <h1 class="slogan">
      <span class="strong">The Good Lord</span>
      <span>does ALL the healing..</span>
      <span>But we DO collect</span>
      <span class="strong">the co-pay</span>
    </h1>

    <div class="clinic-mark" aria-hidden="true"></div>
    <div class="clinic-name">Dunleavy</div>
    <div class="clinic-type">Orthopedic Clinic</div>
  </main>
</body>
</html>
```